Talon Burke Construction LLC

I like to have a business card the is unique, very professional and the it will projected the best first impression of me and my company

Target Market(s)

Remodeling, new constitution

Industry/Entity Type

Business

Font styles to use
Script

Requirements
Must have
• My company name email and phone number
Nice to have
• A logo maybe

```html
<!DOCTYPE html>
<html lang="en">
<head>
<meta charset="UTF-8">
<title>Talon Burke Construction LLC – Business Card</title>
<link href="https://fonts.googleapis.com/css2?family=Montserrat:wght@400;500;600;700&display=swap" rel="stylesheet">
<style>
  :root {
    --bg: #dcdcdc;
    --card-light: #f4f4f2;
    --card-dark: #24262a;
    --orange: #ec8a0c;
    --grey-text: #4a4a4a;
    --rule: #b9b9b9;
    --white: #ffffff;
    --rule-dark: #4a4d52;
  }
  * { margin: 0; padding: 0; box-sizing: border-box; }
  html, body { width: 1200px; height: 900px; overflow: hidden; }
  body {
    background: var(--bg);
    font-family: "Montserrat", sans-serif;
    position: relative;
  }
  .card {
    position: absolute;
    left: 320px;
    width: 560px;
    height: 320px;
    background: var(--card-light);
    box-shadow: 0 6px 18px rgba(0,0,0,0.12);
    overflow: hidden;
  }
  .card-front { top: 100px; }
  .card-back { top: 480px; }

  .brand {
    position: absolute;
    display: flex;
    align-items: center;
    gap: 12px;
  }
  .brand-mark {
    width: 34px;
    height: 34px;
    background: var(--orange);
    border-radius: 4px;
    flex: none;
  }
  .brand-name {
    color: var(--orange);
    font-weight: 600;
    font-size: 22px;
    line-height: 1.15;
    letter-spacing: 0.3px;
  }
  .card-front .brand {
    left: 50%;
    top: 118px;
    transform: translateX(-50%);
  }
  .card-front .brand-name { font-size: 24px; white-space: nowrap; }
  .front-rule {
    position: absolute;
    left: 60px;
    right: 40px;
    top: 232px;
    height: 1px;
    background: var(--rule);
  }

  .card-back .brand { left: 28px; top: 70px; }
  .card-back .brand-name { font-size: 19px; width: 190px; }
  .back-shapes { position: absolute; inset: 0; }

  .holder {
    position: absolute;
    left: 390px;
    top: 74px;
    color: var(--white);
    font-size: 15px;
    letter-spacing: 0.4px;
    text-transform: uppercase;
  }
  .holder-first { font-weight: 700; }
  .holder-last { font-weight: 400; }
  .holder-role {
    display: block;
    text-align: right;
    color: var(--orange);
    font-size: 11px;
    text-transform: none;
    letter-spacing: 0;
    margin-top: 2px;
  }
  .contact {
    position: absolute;
    left: 395px;
    width: 145px;
    color: #d9d9d9;
    font-size: 12px;
    padding-bottom: 10px;
    border-bottom: 1px solid var(--rule-dark);
  }
  .contact-email { top: 150px; }
  .contact-phone { top: 198px; }
</style>
</head>
<body>

  <section class="card card-front">
    <div class="brand">
      <span class="brand-mark"></span>
      <span class="brand-name">Talon Burke Construction LLC</span>
    </div>
    <div class="front-rule"></div>
  </section>

  <section class="card card-back">
    <svg class="back-shapes" width="560" height="320" viewBox="0 0 560 320">
      <polygon points="350,0 560,0 560,320 200,320 350,100" fill="var(--card-dark)"/>
      <polygon points="328,0 344,0 344,104 328,128" fill="var(--orange)"/>
      <rect x="296" y="150" width="38" height="34" fill="var(--orange)"/>
      <rect x="270" y="196" width="38" height="34" fill="var(--orange)"/>
      <g fill="none" stroke="var(--white)" stroke-width="1.6">
        <rect x="306" y="160" width="18" height="13" rx="1"/>
        <polyline points="306,161 315,168 324,161"/>
      </g>
      <path d="M282 206 q3 -2 5 1 l2 3 q1 2 -1 3 l-1 1 q2 4 6 6 l1 -1 q1 -2 3 -1 l3 2 q3 2 1 5 q-2 3 -6 2 q-9 -3 -14 -12 q-2 -5 1 -9z" fill="var(--white)"/>
    </svg>

    <div class="brand">
      <span class="brand-mark"></span>
      <span class="brand-name">Talon Burke Construction LLC</span>
    </div>

    <p class="holder">
      <span class="holder-first">Marcus</span> <span class="holder-last">Hale</span>
      <span class="holder-role">Manager</span>
    </p>
    <p class="contact contact-email">info@talonburke.com</p>
    <p class="contact contact-phone">123 456 789</p>
  </section>

</body>
</html>
```